Luxury Courtside Estate/academy - Webdesign

We want to develop a cutting edge website for a luxury tennis academy. Academy is based in Russia and includes all the necessary amenities for comfortable stay: apartments, spa, tennis courts, training facilities, etc.
We would like to see a clean, simple and modern design (with implementation of all the current trends in web design, although our project has to be distinct and unique).
Color scheme: we would like to see colors present in our logos and all the current associated with tennis. We are open to your ideas and creativity on this front.
The final design should communicate simplicity, be user friendly and convey premium feel.
We woud like to see unique ideas in the design, unconventional techniques, etc.
We don't want standard template design!
Updates
We want to mention that this Tennis Academy has a light focus on nature, as the new material we have uploaded illustrates.
Additional comment to everyone!
We couldn't upload this file to the system: it is too big.
Thank you everyone for your submissions!
Industry/Entity Type
Training
Requirements
Must have
- We would like to see the designs for the following pages:
Home Page:
- Slideshow
- Short description and all the standard stuff
About Us:
- Description with some images
Services:
- Simple description of all of the provided services and possibility to book all of them on the website
! Important ! Develop small system for booking of the days of stay and registration for the courses
Booking and registration !
News:
- Creative layout to display recent news of the academy
Coaches:
- Image and short description of our staff.
Club / Gallery:
- Images and descriptions of the amenities in the territory.
We want a unique display of images: not just lines and rows filled with images
- One idea: an interactive map that displays images and description on mouseover or click on the object on the map (but again, we are open to all your ideas)
Contacts:
- Contact form, contacts, etc.
Sport Store:
- Basic layout for the goods and services provided by the sports store located in the academy
Prices:
- Price lists and ranges with a button leading to registration and booking
For pages like About Us and Services, it would be enough to develop one unified layout for all of them.

```html
<!DOCTYPE html>
<html lang="en">
<head>
<meta charset="utf-8">
<title>Courtside Estate – Home</title>
<link href="https://fonts.googleapis.com/css2?family=Oswald:wght@500;700&family=Montserrat:wght@400;600;700&display=swap" rel="stylesheet">
<style>
:root{
  --bg-dark:#0b150d;
  --green:#1f8c3a;
  --green-dark:#0f5a24;
  --green-bright:#3fbf4a;
  --lime:#8dc63f;
  --yellow:#e8ee1c;
  --orange:#f39a1e;
  --text:#555;
  --text-light:#888;
  --panel:#fff;
  --line:#dcdcdc;
  --field:#0f3018;
}
*{box-sizing:border-box;margin:0;padding:0}
html,body{width:675px;height:1200px;overflow:hidden}
body{position:relative;background:var(--bg-dark);font-family:"Montserrat",Arial,sans-serif;color:var(--text)}
.abs{position:absolute}
.header-scene{left:0;top:0;width:675px;height:340px;background:linear-gradient(180deg,#2f3e2c 0%,#1e2c1f 45%,#0b150d 100%)}
.social-ribbons{right:80px;top:0;display:flex;gap:4px}
.social-ribbons span{display:block;width:17px;height:28px;background:#4a8fc9;clip-path:polygon(0 0,100% 0,100% 100%,50% 80%,0 100%)}
.social-ribbons span+span{background:#6fc3e8}
.logo-tab{left:250px;top:18px;width:176px;height:52px;background:linear-gradient(#fff,#e6e6e6);border-radius:14px 14px 0 0;display:flex;align-items:center;justify-content:center}
.logo-tab .name{font-family:"Oswald",sans-serif;font-weight:700;font-size:19px;color:var(--green);letter-spacing:.3px}
.main-nav{left:79px;top:67px;width:516px;height:30px;background:linear-gradient(#35a947,#127a2c);border-radius:3px;display:flex;align-items:center;justify-content:space-around;box-shadow:0 2px 4px rgba(0,0,0,.5)}
.main-nav a{font-family:"Oswald",sans-serif;font-weight:500;font-size:11.5px;color:#fff;text-decoration:none}
.hero{left:80px;top:115px;width:515px;height:203px;border:3px solid #2a3a2a;background:linear-gradient(180deg,#8fc1e6 0%,#cfe4f2 35%,#b9b9a8 50%,#a55a37 72%,#2f6e2e 100%)}
.hero-title{left:88px;top:274px;font-family:"Oswald",sans-serif;font-weight:700;transform:skewX(-10deg);line-height:.95}
.hero-title .pre{display:block;color:var(--yellow);font-size:18px}
.hero-title .main{display:block;color:var(--green-bright);font-size:31px;letter-spacing:.3px}
.content-panel{left:79px;top:330px;width:516px;height:718px;background:var(--panel);border-radius:4px}
.intro{left:92px;top:341px;width:318px;font-size:7.1px;line-height:1.72;color:var(--text-light)}
.section-title{font-family:"Oswald",sans-serif;font-weight:700;color:var(--green-dark);transform:skewX(-10deg);font-size:13px}
.services-title{left:125px;top:417px;font-size:19px;color:var(--green)}
.photo{display:block}
.card-label{padding:5px 6px;font-size:6.8px;line-height:1.4;color:#fff}
.card-label b{display:block;font-size:9px;font-weight:600;margin-bottom:2px}
.more-link{left:211px;top:636px;font-family:"Oswald",sans-serif;font-weight:700;font-size:9px;color:#222;transform:skewX(-10deg)}
.more-arrow{left:237px;top:633px;width:18px;height:18px;background:#111}
.booking-photo{left:430px;top:340px;width:150px;height:317px;background:linear-gradient(180deg,#e4e8e6 0%,#c9c2b6 35%,#a8543a 70%,#8a3f2c 100%)}
.banner{font-family:"Oswald",sans-serif;font-weight:700;color:#fff;transform:skewX(-10deg);padding:2px 8px;line-height:1.2}
.banner-booking{left:428px;top:343px;background:var(--green);font-size:18px}
.banner-reg{left:448px;top:371px;background:var(--green-dark);font-size:18px}
.block-head{height:22px;border-bottom:1px solid var(--line);display:flex;justify-content:space-between;align-items:flex-end;padding-bottom:5px}
.view-more{font-family:"Oswald",sans-serif;font-weight:700;font-size:9px;color:#aaa;transform:skewX(-10deg)}
.gallery-collage{left:92px;top:728px;width:232px;height:114px;background:linear-gradient(90deg,#b9a67a,#6d8f5c 30%,#d9c89a 55%,#5a4b43 80%,#c2b8b0)}
.avatar{left:85px;top:903px;width:43px;height:43px;background:linear-gradient(#a58a74,#6c5546)}
.quote{left:133px;top:900px;width:199px;height:116px;background:#f1f1f1;border-radius:8px;padding:12px 12px;font-size:6.9px;line-height:1.7;color:#666}
.quote .who{text-align:right;color:var(--green);font-weight:600;margin-top:7px;font-size:7.3px}
.news-item{left:347px;width:245px;height:96px;border-bottom:1px solid #eee}
.news-thumb{position:absolute;left:6px;top:0;width:87px;height:58px;background:linear-gradient(#d2e5ef,#6d9a52 55%,#3f6d2c);box-shadow:0 3px 4px rgba(0,0,0,.25)}
.news-text{position:absolute;left:102px;top:0;width:140px;font-size:6.4px;line-height:1.6;color:#666}
.news-text h3{font-size:8.8px;font-weight:600;color:#333;line-height:1.35;margin-bottom:3px}
.news-text .read{color:#2b6ea8;font-size:6.5px}
.footer-head{font-size:8.5px;color:var(--lime);font-weight:400;letter-spacing:.3px}
.footer-links{font-size:6.6px;color:#9dab9d;line-height:16px;list-style:none}
.footer-links li::before{content:"› ";color:var(--lime)}
.field{background:var(--field);border-radius:3px;font-size:7px;color:#b8c4b8;padding:6px 6px}
.submit{left:337px;top:1129px;width:29px;height:40px;background:var(--field);border-radius:3px}
.connect-row{display:flex;align-items:center;gap:7px;font-size:6.8px;color:#9dab9d;margin-bottom:7px}
.connect-row span{width:15px;height:15px;border-radius:2px;background:#4f7fa8}
.contact-info{font-size:6.5px;color:#9dab9d;line-height:1.55}
.contact-info b{color:#c5d0c5;font-weight:600}
.bottom-bar{left:0;top:1183px;width:675px;height:17px;background:#1a2b12;text-align:center;font-size:6.5px;color:#7d8b6e;line-height:17px}
</style>
</head>
<body>

<div class="abs header-scene" role="img" aria-label="Collage of academy photos: guests, courts and lounge interiors, darkened behind the header"></div>
<div class="abs social-ribbons"><span></span><span></span></div>
<div class="abs logo-tab"><span class="name">Courtside Estate</span></div>

<nav class="abs main-nav">
  <a href="#">HOME</a><a href="#">ABOUT US</a><a href="#">SERVICES</a><a href="#">NEWS</a><a href="#">COACHES</a><a href="#">CLUB / GALLERY</a><a href="#">CONTACTS</a><a href="#">SPORT STORE</a><a href="#">PRICES</a>
</nav>

<div class="abs hero" role="img" aria-label="Clay tennis courts with club houses and an air dome under a blue sky"></div>
<h1 class="abs hero-title"><span class="pre">WELCOME TO</span><span class="main">COURTSIDE ESTATE</span></h1>

<main class="abs content-panel"></main>

<p class="abs intro">Lorem ipsum dolor sit amet, consectetur adipisicing elit, sed do eiusmod tempor incididunt ut labore et dolore magna aliqua. Ut enim ad minim veniam, quis nostrud exercitation ullamco laboris nisi ut aliquip ex ea commodo consequat. Duis aute irure dolor in reprehenderit in voluptate velit esse cillum dolore eu fugiat nulla pariatur.</p>

<h2 class="abs section-title services-title">OUR SERVICES</h2>
<div class="abs" style="left:123px;top:445px;width:122px">
  <div class="photo" style="height:133px;background:linear-gradient(#8c6a4a,#5e4331)" role="img" aria-label="Rider on a horse in an indoor arena"></div>
  <div class="card-label" style="background:var(--green);height:55px"><b>Horse Riding</b>Lorem ipsum dolor sit amet, consectetur adipisicing elit, sed do eiusmod tempor incididunt.</div>
</div>
<div class="abs" style="left:245px;top:433px;width:132px;border-radius:0 14px 8px 0;overflow:hidden;box-shadow:2px 3px 6px rgba(0,0,0,.25)">
  <div class="photo" style="height:134px;background:linear-gradient(#c8d9a8,#5b8a33 60%,#3d6a25)" role="img" aria-label="Sunlit pine forest with green grass"></div>
  <div class="card-label" style="background:var(--orange);height:55px"><b>Forest</b>Lorem ipsum dolor sit amet, consectetur adipisicing elit, sed do eiusmod tempor incididunt.</div>
</div>
<span class="abs more-link">MORE</span>
<svg class="abs more-arrow" viewBox="0 0 18 18"><path d="M5 9h8M10 6l3 3-3 3" stroke="#fff" stroke-width="1.2" fill="none"/></svg>

<div class="abs booking-photo" role="img" aria-label="Two tennis players with rackets on a clay court"></div>
<div class="abs banner banner-booking">BOOKING</div>
<div class="abs banner banner-reg">REGISTRATION !</div>

<div class="abs block-head" style="left:85px;top:689px;width:245px"><h2 class="section-title">CLUB / GALLERY</h2><span class="view-more">VIEW MORE ›</span></div>
<div class="abs gallery-collage" role="img" aria-label="Fanned collage of club photos: lounge, gym, players and grounds"></div>

<div class="abs block-head" style="left:85px;top:872px;width:245px"><h2 class="section-title">TESTIMONIAL</h2><span class="view-more">VIEW MORE ›</span></div>
<div class="abs avatar" role="img" aria-label="Guest portrait"></div>
<blockquote class="abs quote">“Lorem ipsum dolor sit amet, consectetur adipisicing elit, sed do eiusmod tempor incididunt ut labore et dolore magna aliqua. Ut enim ad minim veniam, quis nostrud exercitation ullamco laboris nisi ut aliquip ex ea commodo consequat. Duis aute irure dolor in reprehenderit”<div class="who">JOHN DOE</div></blockquote>

<div class="abs block-head" style="left:347px;top:689px;width:245px"><h2 class="section-title">LATEST NEWS</h2><span class="view-more">VIEW MORE ›</span></div>
<article class="abs news-item" style="top:728px"><div class="news-thumb" role="img" aria-label="Park with trees"></div><div class="news-text"><h3>Lorem ipsum dolor sit amet, consectetur adipiscing elit.</h3>Lorem ipsum dolor sit amet, consectetur adipisicing elit, sed do eiusmod tempor incididunt ut labore et dolore magna aliqua.<div class="read">Read more ›</div></div></article>
<article class="abs news-item" style="top:827px"><div class="news-thumb" role="img" aria-label="Park with trees"></div><div class="news-text"><h3>Lorem ipsum dolor sit amet, consectetur adipiscing elit.</h3>Lorem ipsum dolor sit amet, consectetur adipisicing elit, sed do eiusmod tempor incididunt ut labore et dolore magna aliqua.<div class="read">Read more ›</div></div></article>
<article class="abs news-item" style="top:931px;border:none"><div class="news-thumb" role="img" aria-label="Park with trees"></div><div class="news-text"><h3>Lorem ipsum dolor sit amet, consectetur adipiscing elit.</h3>Lorem ipsum dolor sit amet, consectetur adipisicing elit, sed do eiusmod tempor incididunt ut labore et dolore magna aliqua.<div class="read">Read more ›</div></div></article>

<footer>
  <h4 class="abs footer-head" style="left:80px;top:1063px">QUICK LINK'S</h4>
  <ul class="abs footer-links" style="left:80px;top:1084px"><li>Home</li><li>About Us</li><li>Services</li><li>News</li><li>Coaches</li></ul>
  <ul class="abs footer-links" style="left:127px;top:1084px"><li>Club / Gallery</li><li>Contacts</li><li>Sport Store</li><li>Prices</li></ul>

  <h4 class="abs footer-head" style="left:206px;top:1063px">QUICK CONTACT</h4>
  <div class="abs field" style="left:206px;top:1083px;width:160px;height:20px">Name</div>
  <div class="abs field" style="left:206px;top:1106px;width:160px;height:20px">E-mail</div>
  <div class="abs field" style="left:206px;top:1129px;width:128px;height:40px">Message</div>
  <svg class="abs submit" viewBox="0 0 29 40"><path d="M11 12l8 8-8 8" stroke="var(--lime)" stroke-width="3" fill="none"/></svg>

  <h4 class="abs footer-head" style="left:393px;top:1063px">CONNECT</h4>
  <div class="abs" style="left:393px;top:1086px">
    <div class="connect-row"><span></span>Chirper</div>
    <div class="connect-row"><span></span>Friendbook</div>
  </div>

  <h4 class="abs footer-head" style="left:486px;top:1063px">CONTACT INFO</h4>
  <div class="abs contact-info" style="left:486px;top:1084px;width:125px">
    <b>Courtside Estate</b><br>Lorem ipsum dolor sit amet,<br>secte adipiscing laoreet elit,<br>sed do eiusmod tempor incididunt.
    <div style="margin-top:7px;padding-left:2px">Phone:&nbsp;&nbsp; +1 100 555 0147<br>FAX:&nbsp;&nbsp;&nbsp;&nbsp;&nbsp;&nbsp; +1 200 555 0192<br>E-mail:&nbsp;&nbsp; mail@courtsideestate.com</div>
  </div>
</footer>
<div class="abs bottom-bar">©2012 Courtside Estate</div>

</body>
</html>
```